we need a business card design that shows the customer what we can do for them, in pictures and words. we do tipper work of supplying recycled aggregates, soil removal from site, landscaping, demolition & groundwork and much more.(you can find photo`s and a description on our web site - brackleyplant.co.uk)

brackley plant works ltd, family business doing all aspect`s of machine & tipper lorry work.

```html
<!DOCTYPE html>
<html lang="en">
<head>
<meta charset="utf-8">
<title>Brackley Plant Works Ltd – Business Card</title>
<link rel="stylesheet" href="https://fonts.googleapis.com/css2?family=Archivo:wght@700;800;900&display=swap">
<style>
  :root {
    --brand-blue: #2d55a8;
    --brand-red: #e4312a;
    --card-white: #ffffff;
    --page-bg: #d9d9d9;
  }
  html, body {
    margin: 0;
    width: 1200px;
    height: 900px;
    overflow: hidden;
    background: var(--page-bg);
    font-family: "Archivo", Arial, sans-serif;
  }
  .business-card {
    position: absolute;
    left: 75px;
    top: 150px;
    width: 1050px;
    height: 600px;
    background: var(--card-white);
    overflow: hidden;
    box-shadow: 0 6px 18px rgba(0,0,0,0.25);
  }
  .card-art {
    position: absolute;
    inset: 0;
  }
  .company-name {
    position: absolute;
    left: 250px;
    top: 52px;
    margin: 0;
    font-size: 44px;
    line-height: 1;
    font-weight: 900;
    color: var(--brand-blue);
    white-space: nowrap;
  }
  .tagline {
    position: absolute;
    left: 252px;
    top: 108px;
    margin: 0;
    font-size: 19px;
    font-weight: 800;
    color: var(--brand-red);
    white-space: nowrap;
  }
  .brand-mark {
    position: absolute;
    left: 40px;
    top: 110px;
    width: 190px;
    display: flex;
    flex-direction: column;
    align-items: flex-start;
    gap: 12px;
  }
  .brand-mark__square {
    width: 56px;
    height: 56px;
    background: var(--brand-red);
  }
  .brand-mark__name {
    font-size: 40px;
    line-height: 1.05;
    font-weight: 900;
    color: var(--brand-blue);
  }
  .contact {
    position: absolute;
    right: 40px;
    top: 146px;
    text-align: right;
    font-weight: 800;
    font-style: normal;
  }
  .contact__name {
    font-size: 36px;
    color: var(--brand-blue);
    display: flex;
    align-items: center;
    justify-content: flex-end;
    gap: 10px;
  }
  .contact__line {
    font-size: 25px;
    color: var(--brand-red);
    display: flex;
    align-items: center;
    justify-content: flex-end;
    gap: 10px;
    margin-top: 2px;
  }
  .contact__email {
    margin-top: 12px;
  }
  .icon {
    width: 24px;
    height: 24px;
    flex: none;
  }
  .services {
    position: absolute;
    left: 40px;
    top: 350px;
    margin: 0;
    padding: 0;
    list-style: none;
    font-size: 31px;
    line-height: 1.08;
    font-weight: 800;
    color: var(--brand-red);
  }
</style>
</head>
<body>
  <section class="business-card" aria-label="Brackley Plant Works Ltd business card">
    <svg class="card-art" width="1050" height="600" viewBox="0 0 1050 600">
      <defs>
        <linearGradient id="photo-stone" x1="0" y1="0" x2="0" y2="1">
          <stop offset="0" stop-color="#c9c3bb"/><stop offset="1" stop-color="#8c857c"/>
        </linearGradient>
        <linearGradient id="photo-digger" x1="0" y1="0" x2="0" y2="1">
          <stop offset="0" stop-color="#e2e6ea"/><stop offset="0.5" stop-color="#6b7040"/><stop offset="1" stop-color="#7a6f60"/>
        </linearGradient>
        <linearGradient id="photo-tree" x1="0" y1="0" x2="0" y2="1">
          <stop offset="0" stop-color="#8fb4d8"/><stop offset="0.5" stop-color="#3f5a2c"/><stop offset="1" stop-color="#6b5e4b"/>
        </linearGradient>
        <linearGradient id="photo-lorry" x1="0" y1="0" x2="0" y2="1">
          <stop offset="0" stop-color="#6f8fb5"/><stop offset="0.5" stop-color="#24408c"/><stop offset="1" stop-color="#3a3a3a"/>
        </linearGradient>
        <linearGradient id="photo-paving" x1="0" y1="0" x2="0" y2="1">
          <stop offset="0" stop-color="#b8a98f"/><stop offset="1" stop-color="#8a8a86"/>
        </linearGradient>
        <linearGradient id="photo-slab" x1="0" y1="0" x2="0" y2="1">
          <stop offset="0" stop-color="#6f98c8"/><stop offset="0.4" stop-color="#dfe5e8"/><stop offset="1" stop-color="#b9bfc2"/>
        </linearGradient>
        <linearGradient id="photo-van" x1="0" y1="0" x2="0" y2="1">
          <stop offset="0" stop-color="#7d8a6a"/><stop offset="0.5" stop-color="#eceff1"/><stop offset="1" stop-color="#5c5248"/>
        </linearGradient>
      </defs>

      <polygon class="band band--red" points="0,28 360,28 380,0 0,0" fill="var(--brand-red)"/>
      <polygon class="band band--blue" points="380,0 1050,0 1050,22 362,22" fill="var(--brand-blue)"/>

      <g class="photo-strips">
        <polygon points="540,370 605,370 529,600 464,600" fill="url(#photo-stone)" role="img" aria-label="Photo: pile of recycled aggregate"/>
        <polygon points="615,350 680,350 597,600 532,600" fill="url(#photo-digger)" role="img" aria-label="Photo: excavator working on site"/>
        <polygon points="690,330 755,330 666,600 601,600" fill="url(#photo-tree)" role="img" aria-label="Photo: landscaped site with trees"/>
        <polygon points="765,310 830,310 734,600 669,600" fill="url(#photo-lorry)" role="img" aria-label="Photo: blue tipper lorry loading"/>
        <polygon points="840,295 905,295 804,600 739,600" fill="url(#photo-paving)" role="img" aria-label="Photo: groundworks and paving"/>
        <polygon points="915,280 980,280 874,600 809,600" fill="url(#photo-slab)" role="img" aria-label="Photo: concrete base slab"/>
        <polygon points="990,270 1050,270 1050,600 881,600" fill="url(#photo-van)" role="img" aria-label="Photo: company van on site"/>
      </g>

      <polygon class="band band--blue" points="0,545 600,545 560,600 0,600" fill="var(--brand-blue)"/>
      <polygon class="band band--red" points="575,535 1050,455 1050,600 535,600" fill="var(--brand-red)"/>
    </svg>

    <div class="brand-mark">
      <span class="brand-mark__square" aria-hidden="true"></span>
      <span class="brand-mark__name">Brackley Plant</span>
    </div>

    <h1 class="company-name">BRACKLEY PLANT WORKS LTD</h1>
    <p class="tagline">Family business doing all aspect`s of machine &amp; tipper lorry work.</p>

    <address class="contact">
      <div class="contact__name">Thomas Whitfield
        <svg class="icon" viewBox="0 0 24 24" aria-hidden="true"><circle cx="12" cy="12" r="12" fill="var(--brand-blue)"/><path d="M8 6.5l2 .2 1 3-1.4 1.2a8 8 0 0 0 3.5 3.5l1.2-1.4 3 1 .2 2c-.5 1-1.6 1.5-2.7 1.3A10 10 0 0 1 6.7 9.2C6.5 8.1 7 7 8 6.5z" fill="#fff"/></svg>
      </div>
      <div class="contact__line">07700900461
        <svg class="icon" viewBox="0 0 24 24" aria-hidden="true"><circle cx="12" cy="12" r="12" fill="var(--brand-blue)"/><rect x="6" y="8" width="12" height="9" rx="1" fill="#fff"/><path d="M6.5 8.5l5.5 4.5 5.5-4.5" stroke="var(--brand-blue)" stroke-width="1.5" fill="none"/></svg>
      </div>
      <div class="contact__line contact__email">brackleyplant@mailbox.co.uk</div>
    </address>

    <ul class="services">
      <li>Land Restoration</li>
      <li>Groundworks</li>
      <li>Grab &amp; Tipper Hire</li>
      <li>Demolition</li>
      <li>Recycled Materials</li>
    </ul>
  </section>
</body>
</html>
```